Tea Brand needs a packaging design

We need a Tea packaging design for a new tea brand based in Kenya called 'Vela Tea'. Kenya is home to the finest teas in the world and Vela tea looks to embody that fact. Vela Tea uses the most premium of Kenyan Tea, Black tea, Purple tea, White Tea, Green tea, Hibiscus Tea and Moringa Tea. Vela Tea is handpicked from Kenya's highlands. This project will include the look and feel of the different teas described above. The copy on the main face of the box should read 'Premium Kenyan Tea' The box will contain 25 tagged tea bags, with a net weight of 50 gms. On one side of the box will read 'packaging instructions' To fully savour this Vela premium tea, use one tea bag for each cup, add some freshly bolded water and wait for 2 minutes as you enjoy the sweet aroma of our tea, stir and serve' Ingredients : Black Tea, and for the others the same : Hibiscus Tea, Green Tea, Purple Tea, White tea. should also feature on the label: Produce of Kenya.

Target Market(s)

Premium Market, Global Brand so must have a premium look and feel

Industry/Entity Type

Retail

Font styles to use
Script

Requirements
Must have
• Some natural , earthy feel, a touch of Africa.
Nice to have
• I'd like the package to have a simple and clean look
Should not have
• Should not have a cup of tea. green and yellow should not be the dominant colours

```html
<!DOCTYPE html>
<html lang="en">
<head>
<meta charset="utf-8">
<title>Vela Teas – Premium Kenyan Tea Box</title>
<link rel="stylesheet" href="https://fonts.googleapis.com/css2?family=Playfair+Display:wght@700;800&family=Kaushan+Script&family=Oswald:wght@500&display=swap">
<style>
  :root {
    --earth-brown: #523537;
    --deep-black: #0a0a0b;
    --silver-light: #f2f2f2;
    --silver-mid: #b9b9b9;
    --silver-dark: #7c7c7c;
    --paper-white: #ffffff;
    --brand-brown: #5a3a36;
    --cream-text: #f6f0ea;
  }
  * { margin: 0; padding: 0; box-sizing: border-box; }
  html, body {
    width: 1200px; height: 752px; overflow: hidden;
    background: var(--earth-brown);
  }
  .box-label {
    position: relative; width: 1200px; height: 752px;
    background: var(--earth-brown); overflow: hidden;
  }
  .weight-badge {
    position: absolute; left: 0; top: 0; width: 132px; height: 66px;
    background: var(--deep-black); border-bottom-right-radius: 26px;
    color: var(--silver-light);
    font: 500 28px/66px "Oswald", sans-serif; text-align: center;
    letter-spacing: 0.5px;
  }
  .weight-badge span { border-bottom: 2px solid var(--silver-mid); }
  .mandala-ornament {
    position: absolute; left: 132px; top: 52px; width: 496px; height: 496px;
    border-radius: 50%;
    background: radial-gradient(circle, rgba(230,230,230,0.35) 0%, rgba(200,200,200,0.22) 55%, rgba(180,180,180,0.12) 100%);
  }
  .front-logo-panel {
    position: absolute; left: 200px; top: 136px; width: 360px; height: 280px;
    border-radius: 58px; padding: 10px;
    background: linear-gradient(135deg, var(--silver-light), var(--silver-dark) 45%, var(--silver-light) 70%, var(--silver-mid));
  }
  .front-logo-panel .panel-inner {
    width: 100%; height: 100%; border-radius: 50px; background: var(--paper-white);
    display: flex; align-items: center; justify-content: center;
  }
  .brand-name {
    font-family: "Playfair Display", serif; font-weight: 700;
    color: var(--brand-brown); letter-spacing: 2px;
  }
  .front-logo-panel .brand-name { font-size: 70px; }
  .leaf-decoration {
    position: absolute; left: 542px; top: 486px; width: 190px; height: 120px;
    border-radius: 60% 60% 0 0;
    background: linear-gradient(160deg, var(--silver-mid), var(--deep-black) 40%);
  }
  .fold-line {
    position: absolute; left: 755px; top: 0; height: 752px;
    border-left: 3px dashed var(--paper-white);
  }
  .front-band {
    position: absolute; left: 0; top: 598px; width: 1200px; height: 146px;
    background: var(--deep-black);
    border-top: 10px solid var(--silver-mid);
    border-image: linear-gradient(90deg, var(--silver-dark), var(--silver-light) 40%, var(--silver-dark) 70%, var(--silver-light)) 1;
  }
  .bottom-rule {
    position: absolute; left: 0; top: 744px; width: 1200px; height: 8px;
    background: linear-gradient(90deg, var(--silver-dark), var(--silver-light), var(--silver-dark));
  }
  .tagline {
    position: absolute; left: 96px; top: 628px; width: 580px;
    font-family: "Kaushan Script", cursive; font-size: 60px; line-height: 1.2;
    background: linear-gradient(180deg, #ffffff 10%, #c9c9c9 55%, #8d8d8d);
    -webkit-background-clip: text; background-clip: text; color: transparent;
    white-space: nowrap;
  }
  .side-panel-copy {
    position: absolute; left: 789px; top: 62px; width: 379px;
    color: var(--cream-text);
    font-family: "Playfair Display", serif; font-weight: 800;
    font-size: 20px; line-height: 30px; text-align: justify;
  }
  .side-panel-copy p + p { margin-top: 26px; }
  .origin-note {
    position: absolute; left: 780px; top: 426px; width: 400px; text-align: center;
    color: var(--cream-text);
    font: 800 17px/24px "Playfair Display", serif; letter-spacing: 1px;
  }
  .side-logo-panel {
    position: absolute; left: 882px; top: 623px; width: 190px; height: 104px;
    background: var(--paper-white);
    border-radius: 4px 22px 4px 22px;
    display: flex; align-items: center; justify-content: center;
  }
  .side-logo-panel .brand-name { font-size: 34px; }
</style>
</head>
<body>
<main class="box-label">
  <div class="weight-badge"><span>50 GMS</span></div>

  <div class="mandala-ornament" role="img" aria-label="Silver mandala ornament behind the brand panel"></div>

  <div class="front-logo-panel">
    <div class="panel-inner"><span class="brand-name">Vela Teas</span></div>
  </div>

  <div class="leaf-decoration" role="img" aria-label="Pair of black tea leaves with silver edges"></div>

  <div class="fold-line"></div>

  <div class="front-band"></div>
  <div class="bottom-rule"></div>
  <h1 class="tagline">Premium Kenyan Tea</h1>

  <section class="side-panel-copy">
    <p>INSTRUCTION:To fully savour this Vela premium tea, use one tea bag for each cup, add some freshly bolded water and wait for 2 minutes as you enjoy the sweet aroma of our tea, stir and serve'</p>
    <p>INGREDIENTS : Black Tea, and for the others the same : Hibiscus Tea, Green Tea, Purple Tea, White tea.</p>
  </section>
  <p class="origin-note">MADE IN KENYA</p>

  <div class="side-logo-panel"><span class="brand-name">Vela Teas</span></div>
</main>
</body>
</html>
```